Business Card Design Project

I need some business cards with the logo you did for us (attached)
I am looking for a coulourful yet serious business card

We do market research
on the back I want the logo

on the front my name : Corinne Valdessac
position : Manager
address : Brume Analytica Sarl - 27 Rue des tanneurs
1847 Glarency - Switzerland
corinne.valdessac@brumeanalytica.ch
Tel : +4122 934 07 58
Mob France :+33 671 42 8356
Mob Italy +39 347 520 8163

The tree of the logo could also be used alone

THE BACKGROUND COLOR ON THE FRONT HAS TO BE WHITE, ON THE BACK YU CAN TRY OHER COLOUR BUT HOMOGENEOUS (NOT EXPENSIVE TO PRINT)

Target Market(s)

multinational companies or other market research companies

Industry/Entity Type

Market Research

Requirements
Must have
• logo on the back
and all the info above

```html
<!DOCTYPE html>
<html lang="en">
<head>
<meta charset="utf-8">
<title>Brume Analytica business card</title>
<link rel="stylesheet" href="https://fonts.googleapis.com/css2?family=Questrial&family=Didact+Gothic&display=swap">
<style>
  :root {
    --backdrop: #3b2a20;
    --card-white: #ffffff;
    --card-dark: #3a302c;
    --brand-pink: #d0245f;
    --brand-green: #8dc63f;
    --text-light: #f2eeec;
    --rule: #bdb4b0;
  }
  * { margin: 0; padding: 0; box-sizing: border-box; }
  html, body { width: 848px; height: 1200px; overflow: hidden; }
  body {
    background: var(--backdrop);
    font-family: "Questrial", "Didact Gothic", sans-serif;
    position: relative;
  }
  .card {
    position: absolute;
    top: 412px;
    width: 342px;
    height: 222px;
    box-shadow: 0 4px 14px rgba(0,0,0,0.45);
  }
  .card--logo {
    left: 63px;
    background: var(--card-white);
    display: flex;
    align-items: center;
    justify-content: center;
  }
  .brand {
    display: flex;
    align-items: center;
    gap: 10px;
    margin-top: 20px;
  }
  .brand__dot {
    width: 22px; height: 22px;
    border-radius: 50%;
    background: var(--brand-green);
  }
  .brand__name {
    color: var(--brand-pink);
    font-size: 26px;
    letter-spacing: -0.3px;
  }
  .card--contact {
    left: 425px;
    background: var(--card-dark);
    color: var(--text-light);
  }
  .mini-brand {
    position: absolute;
    top: 14px; right: 14px;
    display: flex; align-items: center; gap: 4px;
  }
  .mini-brand__dot { width: 10px; height: 10px; border-radius: 50%; background: var(--brand-green); }
  .mini-brand__name { color: var(--brand-pink); font-size: 9px; }
  .person {
    position: absolute;
    left: 20px; top: 66px;
  }
  .person__name {
    font-size: 20px;
    line-height: 1;
    letter-spacing: 0.2px;
    text-transform: uppercase;
  }
  .person__first { color: var(--brand-pink); font-weight: bold; }
  .person__role { font-size: 14px; line-height: 1.1; }
  .details {
    position: absolute;
    left: 20px; right: 20px; top: 129px;
    font-size: 9px;
    line-height: 13px;
  }
  .details__block { padding: 4px 0 3px; }
  .details__block--phones { border-top: 1.5px solid var(--rule); }
  .details__block--address {
    border-top: 1px dashed var(--rule);
    border-bottom: 1.5px solid var(--rule);
  }
  .label { font-weight: bold; }
  .sep { color: var(--brand-pink); font-weight: bold; padding: 0 4px; }
</style>
</head>
<body>
  <section class="card card--logo">
    <div class="brand">
      <span class="brand__dot"></span>
      <span class="brand__name">brume analytica</span>
    </div>
  </section>

  <section class="card card--contact">
    <div class="mini-brand">
      <span class="mini-brand__dot"></span>
      <span class="mini-brand__name">brume analytica</span>
    </div>
    <div class="person">
      <p class="person__name"><span class="person__first">Corinne</span> Valdessac</p>
      <p class="person__role">Manager</p>
    </div>
    <div class="details">
      <div class="details__block details__block--phones">
        <p><span class="label">Tel :</span> +4122 934 07 58 <span class="label">. Mob France :</span> +33 671 42 8356</p>
        <p><span class="label">Mob Italy :</span> +39 347 520 8163</p>
      </div>
      <div class="details__block details__block--address">
        <p><span class="label">Brume Analytica Sarl</span> . 27 Rue des tanneurs . 1847 Glarency</p>
        <p>Switzerland <span class="sep">//</span><span class="label">email :</span> corinne.valdessac@brumeanalytica.ch</p>
      </div>
    </div>
  </section>
</body>
</html>
```